Flyer Design

Company name Brightgrate, ecofriendly oven cleaning. See website brightgrate.co.uk. Looking for a flyer to offer a 10% discount off web prices Picture of shiny oven, highlighting eco aspect

Industry/Entity Type

It Company

```html
<!DOCTYPE html>
<html lang="en">
<head>
<meta charset="utf-8">
<title>Brightgrate – Eco-Friendly Oven Cleaning Flyer</title>
<link rel="stylesheet" href="https://fonts.googleapis.com/css2?family=Signika:wght@300;400;600;700&family=Oswald:wght@600;700&family=Source+Sans+3:wght@300;400;600;700&display=swap">
<style>
  :root{
    --green:#4aa23c;
    --green-deep:#15873a;
    --green-light:#8cc63f;
    --green-pale:#b5d56b;
    --yellow:#f2e300;
    --ink:#333333;
    --grey:#555555;
    --paper:#ffffff;
  }
  *{margin:0;padding:0;box-sizing:border-box;}
  html,body{width:901px;height:1200px;overflow:hidden;background:var(--paper);}
  .flyer{position:relative;width:901px;height:1200px;background:linear-gradient(#fff 75%,#f4f4f4);font-family:"Source Sans 3",sans-serif;color:var(--ink);overflow:hidden;}
  .abs{position:absolute;}

  .brand-name{left:56px;top:32px;font-family:"Signika",sans-serif;font-weight:700;font-size:50px;color:var(--green-light);letter-spacing:-1px;}
  .brand-tag{left:58px;top:92px;font-family:"Signika",sans-serif;font-weight:600;font-size:16px;color:var(--green-light);}
  .van{left:314px;top:40px;width:136px;height:76px;border-radius:10px;background:linear-gradient(#f4f4f4,#cfcfcf);}
  .brand-url{left:58px;top:124px;font-size:24px;font-weight:300;color:var(--grey);letter-spacing:1px;}

  .hook{right:46px;top:38px;text-align:right;font-family:"Signika",sans-serif;font-weight:600;font-size:31px;line-height:40px;color:var(--green);}
  .hook-sub{right:46px;top:142px;text-align:right;font-size:23px;line-height:32px;font-weight:300;color:var(--grey);}

  .hero{left:0;top:0;}
  .discount{left:112px;top:318px;font-family:"Signika",sans-serif;font-weight:600;font-size:36px;color:var(--green-pale);}
  .look-badge{left:124px;top:362px;width:196px;height:196px;border-radius:50%;background:var(--green-deep);border:5px solid var(--yellow);box-shadow:0 0 0 3px #fff,0 4px 10px rgba(0,0,0,.35);display:flex;align-items:center;justify-content:center;text-align:center;font-family:"Signika",sans-serif;font-weight:600;font-size:27px;line-height:33px;color:#fff;}
  .eco-badge{left:668px;top:382px;width:160px;height:160px;border-radius:50%;background:radial-gradient(circle,#8cc63f 0 45%,#ffffff 46% 50%,var(--green-deep) 51% 86%,#d8b630 87%);}

  .services{left:692px;top:548px;width:170px;height:322px;border-radius:62px;background:var(--green);border:3px solid #fff;box-shadow:0 0 0 2px #c9c9c9;color:#fff;text-align:center;font-size:22px;line-height:34px;padding-top:12px;}

  .headline{left:36px;top:566px;font-family:"Oswald",sans-serif;font-weight:700;font-size:58px;line-height:66px;color:var(--green-deep);letter-spacing:.2px;}
  .intro{left:36px;top:730px;width:580px;font-size:16.5px;line-height:22px;color:var(--ink);}
  .eco-bar{left:0;top:778px;width:614px;height:36px;background:var(--green);border-radius:0 18px 18px 0;color:#fff;font-family:"Signika",sans-serif;font-weight:600;font-size:21px;line-height:36px;padding-left:36px;}

  .list-title{top:842px;font-size:20px;font-weight:600;color:var(--ink);}
  .list{top:880px;list-style:none;font-size:16.5px;line-height:26px;color:var(--ink);}
  .list li{position:relative;padding-left:31px;}
  .list li::before{content:"";position:absolute;left:2px;top:7px;width:14px;height:13px;border-radius:50%;background:radial-gradient(circle at 40% 35%,var(--green-pale),#5a8d1d);}
  .work{left:36px;}
  .benefits{left:448px;}
  .inline-item{position:relative;padding-left:31px;margin-left:26px;}
  .inline-item::before{content:"";position:absolute;left:2px;top:7px;width:14px;height:13px;border-radius:50%;background:radial-gradient(circle at 40% 35%,var(--green-pale),#5a8d1d);}

  .proof{left:40px;top:994px;width:416px;height:156px;background:var(--green-light);}
  .proof-shot{position:absolute;top:6px;width:192px;height:126px;border-radius:8px;}
  .shot-before{left:10px;background:linear-gradient(135deg,#2f2a25,#6b5a48 60%,#3b332b);}
  .shot-after{left:210px;background:linear-gradient(135deg,#5d6266,#c7ccd0 55%,#7b8084);}
  .proof-label{position:absolute;top:134px;width:192px;text-align:center;color:#fff;font-size:15px;}

  .offer{left:485px;top:994px;width:376px;height:42px;background:var(--green-deep);color:#fff;font-size:21px;line-height:42px;padding-left:8px;}
  .offer b{font-weight:700;}
  .prices{right:40px;top:1048px;width:390px;text-align:right;font-size:16px;line-height:24px;color:var(--ink);}
  .call{right:40px;top:1094px;font-family:"Oswald",sans-serif;font-weight:700;font-size:41px;color:var(--ink);}
  .book{right:40px;top:1150px;font-size:18px;color:#111;}

  .contact{left:36px;top:1154px;font-size:17px;color:var(--ink);display:flex;align-items:center;gap:8px;}
  .contact .dot{width:14px;height:13px;border-radius:50%;background:radial-gradient(circle at 40% 35%,var(--green-pale),#5a8d1d);}
  .contact strong{font-size:21px;font-weight:700;color:#111;}
</style>
</head>
<body>
<div class="flyer">

  <svg class="abs hero" width="901" height="600" viewBox="0 0 901 600">
    <defs>
      <linearGradient id="kitchenTone" x1="0" y1="0" x2="0" y2="1">
        <stop offset="0" stop-color="#6a5340"/>
        <stop offset=".35" stop-color="#3b3a39"/>
        <stop offset=".7" stop-color="#2e2d2c"/>
        <stop offset=".85" stop-color="#d9d3c8"/>
        <stop offset="1" stop-color="#e6e1d8"/>
      </linearGradient>
    </defs>
    <rect x="0" y="170" width="901" height="350" fill="url(#kitchenTone)" role="img" aria-label="Photo of a clean modern kitchen with dark worktop and white cabinets"/>
    <path d="M0,0 H901 V190 C800,225 700,215 560,192 C400,165 200,165 0,205 Z" fill="#ffffff"/>
    <path d="M0,205 C200,165 400,165 560,192 C700,215 800,225 901,190 V212 C800,248 700,238 560,214 C400,188 200,195 0,230 Z" fill="#8cc63f"/>
    <path d="M0,455 C200,440 400,500 600,500 C750,500 850,470 901,445 V467 C850,492 750,522 600,522 C400,522 200,472 0,477 Z" fill="#4aa23c"/>
    <path d="M0,477 C200,472 400,522 600,522 C750,522 850,492 901,467 V600 H0 Z" fill="#ffffff"/>
  </svg>

  <div class="abs brand-name">Brightgrate</div>
  <div class="abs brand-tag">eco-friendly oven cleaning</div>
  <div class="abs van" role="img" aria-label="Photo of the white company van"></div>
  <div class="abs brand-url">www.brightgrate.co.uk</div>

  <h2 class="abs hook">Got an oven covered in<br>dirt, grease or grime?</h2>
  <p class="abs hook-sub">Hire the oven cleaning experts<br>and let us do a job you hate!</p>

  <div class="abs discount">10% Discount</div>
  <div class="abs look-badge">Give<br>your oven a<br>great new<br>look!</div>
  <div class="abs eco-badge" role="img" aria-label="Eco friendly seal"></div>

  <div class="abs services">We<br>specialise<br>in cleaning<br>Ovens, Hobs,<br>Extractors,<br>Ranges,<br>Stoves and<br>Barbecues.</div>

  <h1 class="abs headline">Your Local Professional<br>Oven Cleaning Company</h1>
  <p class="abs intro">We are a family run business providing an outstanding and professional oven cleaning service in Poole, Bournemouth and throughout East Dorset.</p>
  <div class="abs eco-bar">We Only Use 100% Environmentally Friendly Products</div>

  <h3 class="abs list-title" style="left:36px;">Work includes:</h3>
  <ul class="abs list work">
    <li>Removal of side panels, racks and shelves</li>
    <li>Heat Treatment of parts in a non-toxic solution</li>
    <li>Main Shell Cleaning using fume-free spray</li>
    <li>Oven cleaning by hand</li>
  </ul>

  <h3 class="abs list-title" style="left:448px;">Oven cleaning benefits:</h3>
  <ul class="abs list benefits">
    <li>Speedy and convenient</li>
    <li>Reliable and reputable</li>
    <li>Cleaning to highest possible standards</li>
    <li>Fume-free systems<span class="inline-item">Sparkling results</span></li>
  </ul>

  <div class="abs proof">
    <div class="proof-shot shot-before" role="img" aria-label="Photo of a dirty oven interior before cleaning"></div>
    <div class="proof-shot shot-after" role="img" aria-label="Photo of a shiny oven interior after cleaning"></div>
    <span class="proof-label" style="left:10px;">Before</span>
    <span class="proof-label" style="left:210px;">After</span>
  </div>

  <div class="abs offer">Offer a <b>10% discount</b> off web prices</div>
  <p class="abs prices">Our oven cleaning prices include all manufacturer supplied trays, shelves and the fan where necessary.</p>
  <div class="abs call">Call: 07700 900418</div>
  <div class="abs book">Book your oven cleaning service today</div>

  <div class="abs contact">hello.brightgrate@mailbox.co.uk <span class="dot"></span> <strong>brightgrate.co.uk</strong></div>
</div>
</body>
</html>
```